Business card

We need a business card design for our company based in Auckland , New Zealand called 'Quill + Habitat Ltd'. We provide architectural services. We would like to see designs that use the max. three colours (such as white, black, grey) The final design should communicate financial safety and growth."
Also I will provide our company logo. I would like to the logo to be embeded onto our business card.

Target Market(s)

new residential house, alteration & addition & light commericila design & drafting service

Industry/Entity Type

Architecture

Contact Information for Business Card

Company name: quill + habitat Ltd.
Name: Rowan Teale
Job title: architectural designer & Design QWR
email address: rowan@qandh.co.nz
mobile number: 02 5136 2297
web site: www.qandh.co.nz

Requirements
Must have
• My project must have..
• - embeded logo (attached company logo)
• I don't have a bigger version for our company logo, but I have one old one, so you can remove the word from it)
• - insert the attached small GVTK logo & QWR logo
• - creative, simple and clear business card.
• - Max. three colours
Nice to have
• - Here are the samples I would like to share with you: http://www.velmoriq.com/blog/sparse-stationery-layouts/
• I would like to have my business card like one of the creation.
Should not have
• TBA

```html
<!DOCTYPE html>
<html lang="en">
<head>
<meta charset="utf-8">
<title>Quill + Habitat Ltd — Business Card</title>
<link href="https://fonts.googleapis.com/css2?family=Montserrat:wght@400;500;600;700&display=swap" rel="stylesheet">
<style>
  :root {
    --backdrop: #2b2b2b;
    --ink: #0a0a0a;
    --paper: #ffffff;
    --grey: #8a8a8a;
    --grey-soft: #d6d6d6;
  }
  * { box-sizing: border-box; margin: 0; padding: 0; }
  html, body {
    width: 1200px; height: 900px; overflow: hidden;
    background: var(--backdrop);
    font-family: "Montserrat", Arial, sans-serif;
  }
  .stage { position: relative; width: 1200px; height: 900px; }
  .card {
    position: absolute; width: 560px; height: 320px;
    border-radius: 22px; overflow: hidden;
    box-shadow: 0 18px 40px rgba(0,0,0,.45);
  }

  /* Front: black */
  .card-front { left: 90px; top: 110px; background: var(--ink); color: var(--paper); }
  .card-front .company {
    position: absolute; left: 40px; bottom: 60px;
    font-size: 22px; font-weight: 600; letter-spacing: .2px;
  }
  .card-front .company .ltd { font-weight: 400; }
  .badges { position: absolute; right: 40px; top: 60px; display: flex; align-items: flex-end; gap: 22px; }
  .badge-member { width: 78px; height: 70px; background: #5a5a55; border-radius: 4px; }
  .badge-practitioner { width: 90px; height: 90px; border-radius: 50%; background: var(--paper); border: 6px solid var(--grey-soft); }
  .card-front .web {
    position: absolute; right: 40px; top: 180px;
    font-size: 20px; font-weight: 400;
  }

  /* Back: white */
  .card-back { left: 550px; top: 470px; background: var(--paper); color: var(--ink); }
  .side-band { position: absolute; left: 0; top: 0; bottom: 0; width: 64px; background: var(--ink); }
  .side-rule { position: absolute; left: 72px; top: 86px; bottom: 0; width: 3px; background: var(--grey); }
  .mark-dot {
    position: absolute; left: 28px; top: 40px; width: 84px; height: 84px;
    border-radius: 50%; background: var(--paper); border: 6px solid var(--ink);
  }
  .card-back .company {
    position: absolute; left: 140px; top: 66px;
    font-size: 19px; font-weight: 600;
  }
  .card-back .company .ltd { font-weight: 400; }
  .person { position: absolute; left: 140px; top: 140px; }
  .person .name { font-size: 26px; font-weight: 700; letter-spacing: .5px; text-transform: uppercase; }
  .person .role { font-size: 15px; line-height: 1.2; margin-top: 2px; }
  .contacts { list-style: none; margin-top: 8px; }
  .contacts li { display: flex; align-items: center; gap: 10px; font-size: 15px; line-height: 22px; }
  .contacts svg { width: 13px; height: 13px; flex: none; }
</style>
</head>
<body>
<main class="stage">

  <section class="card card-front">
    <div class="badges">
      <div class="badge-member" role="img" aria-label="Professional membership badge"></div>
      <div class="badge-practitioner" role="img" aria-label="Licensed practitioner badge"></div>
    </div>
    <p class="web">www.qandh.co.nz</p>
    <p class="company">Quill + Habitat <span class="ltd">Ltd</span></p>
  </section>

  <section class="card card-back">
    <div class="side-band"></div>
    <div class="side-rule"></div>
    <div class="mark-dot"></div>
    <p class="company">Quill + Habitat <span class="ltd">Ltd</span></p>
    <div class="person">
      <h1 class="name">Rowan Teale</h1>
      <p class="role">Architectural designer<br>&amp; Design QWR</p>
      <ul class="contacts">
        <li>
          <svg viewBox="0 0 24 24"><path fill="#0a0a0a" d="M6.6 10.8a15.1 15.1 0 0 0 6.6 6.6l2.2-2.2a1 1 0 0 1 1-.25 11.4 11.4 0 0 0 3.6.57 1 1 0 0 1 1 1V20a1 1 0 0 1-1 1A17 17 0 0 1 3 4a1 1 0 0 1 1-1h3.5a1 1 0 0 1 1 1c0 1.25.2 2.45.57 3.6a1 1 0 0 1-.25 1z"/></svg>
          02 5136 2297
        </li>
        <li>
          <svg viewBox="0 0 24 24"><rect x="2" y="5" width="20" height="14" rx="1" fill="none" stroke="#0a0a0a" stroke-width="2"/><path d="M2 6l10 7 10-7" fill="none" stroke="#0a0a0a" stroke-width="2"/></svg>
          rowan@qandh.co.nz
        </li>
        <li>
          <svg viewBox="0 0 24 24"><circle cx="12" cy="12" r="10" fill="none" stroke="#0a0a0a" stroke-width="2"/><path d="M2 12h20M12 2c3 3 3 17 0 20M12 2c-3 3-3 17 0 20" fill="none" stroke="#0a0a0a" stroke-width="2"/></svg>
          www.qandh.co.nz
        </li>
      </ul>
    </div>
  </section>

</main>
</body>
</html>
```